Commercial snow and summer maintenance marketing folders

I'M looking to design a marketing folder for my snow and summer maintenance company.
The folder is a 12''x9'' , i want to fill up the front and back.
Acquire them for the first,keep them for all time is the slogan that will go somewhere in the front ,
I will attach logo, im thinking to having that in the front,top,middle. having a small logo in back bottom middle of page with phone number 647-319-5520,www.brindlegrounds.com . Proud members of Greenway Guild, Wise With Grit And TCPA with small logos beside them. Small writing underneath "2016 Brindle Grounds Ltd. Independently owned and operated. Propriety and Confidential
B2B, Industrial, commercial and municipal customers
Snow Removal

```html
<!DOCTYPE html>
<html lang="en">
<head>
<meta charset="utf-8">
<title>Brindle Grounds – Folder Front and Back</title>
<link href="https://fonts.googleapis.com/css2?family=Ubuntu:wght@500;700&family=Questrial&family=Oswald:wght@400;500&family=Open+Sans:ital,wght@0,400;0,600;0,700;1,400&display=swap" rel="stylesheet">
<style>
  :root{
    --backdrop:#d8d8d8;
    --paper:#ffffff;
    --green-deep:#2f8a34;
    --green-mid:#3f9d3a;
    --green-lime:#a6cf38;
    --green-pale:#cfe6b8;
    --green-row:#e3f0d8;
    --ink:#3a3a3a;
    --ink-soft:#555;
    --title-shadow:#1c5a20;
  }
  *{margin:0;padding:0;box-sizing:border-box}
  html,body{width:1200px;height:800px;overflow:hidden;background:var(--backdrop)}
  .canvas{position:relative;width:1200px;height:800px}
  .page{position:absolute;top:74px;width:512px;height:660px;background:var(--paper);overflow:hidden}
  .page--front{left:55px}
  .page--back{left:632px}

  .scene-photo,.lawn-photo{position:absolute;left:0;width:100%}
  .scene-photo{top:110px;height:470px;
    background:linear-gradient(180deg,#6b8f4a 0%,#7aa04a 25%,#8fc04c 45%,#a6d060 65%,rgba(220,238,200,.9) 85%,#fff 100%)}
  .lawn-photo{top:120px;height:330px;
    background:linear-gradient(180deg,#7fb54a 0%,#9cc86a 40%,#cfe3b8 75%,#fff 100%)}

  .header-wave{position:absolute;left:0;top:0;width:512px;height:300px}
  .header-title{position:absolute;left:0;width:100%;text-align:center;font-family:'Ubuntu',sans-serif;font-weight:700;
    font-size:35px;color:#fff;letter-spacing:.3px;text-shadow:2px 2px 0 var(--title-shadow)}
  .header-sub{position:absolute;left:0;width:100%;text-align:center;font-family:'Questrial',sans-serif;font-size:22px;
    color:var(--title-shadow);letter-spacing:.5px}

  .brand{position:absolute;left:0;width:100%;display:flex;align-items:center;justify-content:center;gap:10px;
    font-family:'Questrial',sans-serif;color:var(--ink);letter-spacing:3px}
  .brand-square{background:var(--green-mid)}
  .page--front .brand{top:430px;font-size:34px}
  .page--front .brand-square{width:20px;height:20px}
  .page--back .brand{top:500px;font-size:26px}
  .page--back .brand-square{width:15px;height:15px}

  .slogan{position:absolute;left:0;top:490px;width:100%;text-align:center;font-family:'Questrial',sans-serif;
    font-size:15px;color:var(--green-deep);letter-spacing:.4px}

  .legal-name{position:absolute;left:0;width:100%;text-align:center;font-family:'Questrial',sans-serif;color:var(--ink);font-size:19px;letter-spacing:.3px}
  .legal-line{position:absolute;left:0;width:100%;text-align:center;font-family:'Questrial',sans-serif;color:var(--ink);font-size:12px;letter-spacing:.2px}

  .contact-band{position:absolute;left:0;width:100%;height:26px;background:var(--green-lime)}
  .contact-rule{position:absolute;left:0;width:100%;height:3px;background:var(--green-lime)}
  .phone{position:absolute;left:0;width:100%;text-align:center;font-family:'Oswald',sans-serif;color:var(--ink)}
  .web{position:absolute;left:0;width:100%;text-align:center;font-family:'Open Sans',sans-serif;color:var(--ink-soft);letter-spacing:4px}

  .page--front .legal-name{top:562px}
  .page--front .legal-line{top:586px}
  .page--front .contact-band{top:604px}
  .page--front .phone{top:599px;font-size:25px;font-weight:400}
  .page--front .contact-rule{top:633px}
  .page--front .web{top:640px;font-size:9.5px}

  .page--back .legal-name{top:231px}
  .page--back .legal-line{top:256px}
  .page--back .phone{top:560px;font-size:32px;font-weight:500}
  .page--back .contact-band{top:606px}
  .page--back .web{top:611px;font-size:12px;color:var(--ink)}
  .page--back .contact-rule{top:634px}

  .info-table{position:absolute;top:282px;width:196px;font-family:'Open Sans',sans-serif}
  .info-table--left{left:32px}
  .info-table--right{left:284px}
  .info-head{height:22px;background:var(--green-deep);color:#fff;font-weight:700;font-size:11.5px;text-align:center;line-height:22px}
  .info-row{height:23px;line-height:23px;text-align:center;font-size:10px;color:var(--ink-soft);background:var(--green-row)}
  .info-row:nth-child(odd){background:var(--green-pale)}
  .info-row--accent{color:var(--green-deep);font-weight:700;font-size:10.5px}
  .info-table--right .info-row{font-weight:700;color:var(--ink);font-size:10.5px}
  .info-body{margin-top:6px;font-size:7.6px;line-height:1.2;color:var(--ink);text-align:justify}
  .info-body p+p{margin-top:8px}
  .info-note{margin-top:4px;font-size:7.4px;line-height:1.25;color:var(--green-deep);text-align:center}
</style>
</head>
<body>
<main class="canvas">

  <section class="page page--front">
    <div class="scene-photo" role="img" aria-label="Photo of a landscaped front yard with colourful flower beds, shrubs and a striped green lawn in front of a house porch"></div>
    <svg class="header-wave" viewBox="0 0 512 300" aria-hidden="true">
      <defs>
        <linearGradient id="frontTop" x1="0" y1="0" x2="1" y2="0">
          <stop offset="0" stop-color="#8cc63f"/><stop offset=".45" stop-color="#3f9d3a"/><stop offset="1" stop-color="#2f8a34"/>
        </linearGradient>
        <linearGradient id="frontSwoosh" x1="0" y1="0" x2="1" y2="0">
          <stop offset="0" stop-color="#a6cf38"/><stop offset="1" stop-color="#3f9d3a"/>
        </linearGradient>
      </defs>
      <path d="M0 200 C40 240 90 230 130 215 C200 190 220 160 300 140 C390 120 470 170 512 240 V300 C480 220 410 170 320 170 C230 175 160 230 90 238 C50 242 20 232 0 225 Z" fill="url(#frontSwoosh)"/>
      <path d="M0 0 H512 V230 C470 160 400 125 310 132 C220 140 190 180 120 200 C70 214 30 210 0 185 Z" fill="url(#frontTop)"/>
      <path d="M0 185 C30 210 70 214 120 200 C190 180 220 140 310 132 C400 125 470 160 512 230" fill="none" stroke="#e6e6e6" stroke-width="2"/>
    </svg>
    <h1 class="header-title" style="top:47px">GREENWAY GUILD</h1>
    <p class="header-sub" style="top:86px">WISE WITH GRIT AND TCPA</p>

    <div class="brand"><span class="brand-square"></span>BRINDLE GROUNDS</div>
    <p class="slogan">Acquire them for the first, keep them for all time</p>

    <p class="legal-name">2016 BRINDLE GROUNDS LTD</p>
    <p class="legal-line">INDEPENDENTLY OWNED AND OPERATED. PROPRIETY AND CONFIDENTIAL</p>
    <div class="contact-band"></div>
    <p class="phone">647-319-5520</p>
    <div class="contact-rule"></div>
    <p class="web">www.brindlegrounds.com</p>
  </section>

  <section class="page page--back">
    <div class="lawn-photo" role="img" aria-label="Photo of a freshly mowed striped lawn"></div>
    <svg class="header-wave" viewBox="0 0 512 300" aria-hidden="true">
      <defs>
        <linearGradient id="backTop" x1="0" y1="0" x2="1" y2="0">
          <stop offset="0" stop-color="#8cc63f"/><stop offset=".45" stop-color="#3f9d3a"/><stop offset="1" stop-color="#2f8a34"/>
        </linearGradient>
      </defs>
      <path d="M0 180 C30 215 80 215 130 200 C200 178 230 150 310 140 C400 130 470 175 512 235 V250 C470 190 400 155 320 158 C230 165 170 215 100 222 C50 228 20 220 0 212 Z" fill="#a6cf38"/>
      <path d="M0 0 H512 V225 C470 160 400 122 310 128 C220 136 190 170 120 190 C70 202 30 198 0 170 Z" fill="url(#backTop)"/>
      <path d="M0 170 C30 198 70 202 120 190 C190 170 220 136 310 128 C400 122 470 160 512 225" fill="none" stroke="#e6e6e6" stroke-width="2"/>
    </svg>
    <h1 class="header-title" style="top:48px">GREENWAY GUILD</h1>
    <p class="header-sub" style="top:88px">WISE WITH GRIT AND TCPA</p>

    <p class="legal-name">2016 BRINDLE GROUNDS LTD</p>
    <p class="legal-line">INDEPENDENTLY OWNED AND OPERATED. PROPRIETY AND CONFIDENTIAL</p>

    <div class="info-table info-table--left">
      <div class="info-head">LOREM IPSUM IS SIMPLY</div>
      <div class="info-row">simply dummy text of the printing</div>
      <div class="info-row info-row--accent">LOREM IPSUM</div>
      <div class="info-row">simply dummy text of the printing</div>
      <div class="info-row info-row--accent">LOREM IPSUM</div>
      <div class="info-body">
        <p>Lorem Ipsum is simply dummy text of the printing and typesetting industry. Lorem Ipsum has been</p>
        <p>the industry's standard dummy text ever since the 1500s, when an unknown printer took a galley of type and scrambled it to make a type specimen book</p>
      </div>
    </div>

    <div class="info-table info-table--right">
      <div class="info-head">LOREM IPSUM IS DUMMY</div>
      <div class="info-row">Lorem Ipsum</div>
      <div class="info-row">Simply Dumm</div>
      <div class="info-row">Printing and Typesetting</div>
      <div class="info-row">Lorem Ipsum</div>
      <div class="info-row">simply dummy text</div>
      <p class="info-note">Contrary to popular belief, Lorem Ipsum is not<br>simply random text</p>
    </div>

    <div class="brand"><span class="brand-square"></span>BRINDLE GROUNDS</div>
    <p class="phone">647-319-5520</p>
    <div class="contact-band"></div>
    <p class="web">www.brindlegrounds.com</p>
    <div class="contact-rule"></div>
  </section>

</main>
</body>
</html>
```